Vantrel General Painting Ltd. - Construction painting company providing high-quality service

We need a logo and business card design for a painting company that provides high-quality work for major developers and builders in Calgary, Alberta. Our projects include commercial high-rise residential towers. We would like designs that communicate professionalism and high quality service.
Updates
Target Market(s)
Developers and builders
Industry/Entity Type
Construction
Contact Information for Business Card
Company name, employee name, title, phone number, email address
Font styles to use
Colors
Designer to choose colors to be used in the design.
Look and feel
Each slider illustrates characteristics of the customer's brand and the style your logo design should communicate.

```html
<!DOCTYPE html>
<html lang="en">
<head>
<meta charset="utf-8">
<title>Vantrel General Painting Ltd. – Business Card</title>
<link rel="stylesheet" href="https://fonts.googleapis.com/css2?family=Montserrat:wght@500;600;700;800&display=swap">
<style>
  :root {
    --stage: #e9eaee;
    --card-dark: #232323;
    --card-light: #ffffff;
    --navy: #1d1f5c;
    --gold: #f7b51e;
    --sky: #2cb5ea;
  }
  * { box-sizing: border-box; margin: 0; padding: 0; }
  html, body { width: 1200px; height: 880px; overflow: hidden; }
  body {
    background: var(--stage);
    font-family: "Montserrat", sans-serif;
    display: flex; flex-direction: column; align-items: center; justify-content: center;
    gap: 40px;
  }
  .card {
    width: 660px; height: 377px; border-radius: 20px; position: relative;
    box-shadow: 0 12px 30px rgba(0,0,0,.18);
  }
  .card--back {
    background: var(--card-dark);
    display: flex; align-items: center; justify-content: center; gap: 16px;
  }
  .brand-dot { width: 26px; height: 26px; border-radius: 50%; background: var(--sky); flex: none; }
  .brand-name {
    color: var(--gold); font-weight: 700; text-transform: uppercase;
    font-size: 30px; line-height: 1.15; letter-spacing: .5px;
  }
  .card--front { background: var(--card-light); }
  .front-brand {
    position: absolute; left: 48px; top: 96px;
    color: var(--navy); font-weight: 700; text-transform: uppercase;
    font-size: 27px; line-height: 1.15;
  }
  .front-mark {
    position: absolute; right: 78px; top: 50px;
    width: 130px; height: 130px; border-radius: 50%; background: var(--sky);
  }
  .divider {
    position: absolute; left: 40px; right: 40px; top: 262px;
    height: 1.5px; background: var(--navy);
  }
  .person { position: absolute; left: 48px; top: 228px; }
  .person-name { color: var(--navy); font-weight: 800; font-size: 22px; }
  .person-title { color: var(--gold); font-weight: 500; font-size: 17px; margin-top: 14px; }
  .contact {
    position: absolute; right: 44px; top: 282px;
    list-style: none; color: var(--navy); font-weight: 600; font-size: 15px;
  }
  .contact li { display: flex; align-items: center; gap: 10px; margin-bottom: 10px; }
  .contact svg { width: 16px; height: 16px; flex: none; }
</style>
</head>
<body>
  <section class="card card--back">
    <span class="brand-dot"></span>
    <p class="brand-name">Vantrel General<br>Painting Ltd</p>
  </section>

  <section class="card card--front">
    <p class="front-brand">Vantrel General<br>Painting Ltd</p>
    <span class="front-mark"></span>
    <div class="person">
      <p class="person-name">Marcus Hale</p>
      <p class="person-title">Principal</p>
    </div>
    <div class="divider"></div>
    <ul class="contact">
      <li>
        <svg viewBox="0 0 24 24" aria-hidden="true"><path fill="#f7b51e" d="M6.6 10.8a15.1 15.1 0 0 0 6.6 6.6l2.2-2.2c.3-.3.7-.4 1-.2 1.1.4 2.3.6 3.6.6.6 0 1 .4 1 1V20c0 .6-.4 1-1 1A17 17 0 0 1 3 4c0-.6.4-1 1-1h3.5c.6 0 1 .4 1 1 0 1.3.2 2.5.6 3.6.1.3 0 .7-.2 1z"/></svg>
        0453-555-0187
      </li>
      <li>
        <svg viewBox="0 0 24 24" aria-hidden="true"><rect x="2" y="5" width="20" height="14" rx="1.5" fill="#f7b51e"/><path d="M2.5 6l9.5 7 9.5-7" fill="none" stroke="#fff" stroke-width="1.6"/></svg>
        info@vantrelpainting.com
      </li>
    </ul>
  </section>
</body>
</html>
```